I need a simple infographic that describes the 4 basic elements of how to effectively create change.

The overall title (Gentle Pressure Relentlessly Applied) should be at the top of the infographic. Subtitle is: "Leading Change".
There are four steps:
1. Alignment- Agreement on Approach
2. Transparency- Metrics for Assurance
3. Skills- Training and Coaching
4. Integrity- Culture of Accountability

Target Market(s)

Business Leaders in a training workshop

Font styles to use
Serif

Requirements
Must have
• Here are the 4 elements of the Infographic: Please show them in order.
• 1. Agreement on Approach. (Alignment)
• 2. Metrics for Assurance (Transparency)
• 3. Training and Coaching (Skills)
• 4. Culture of Accountability (Integrity)
Nice to have
• Cool Graphics that depict the 4 steps.
Should not have
• Pictures.

```html
<!DOCTYPE html>
<html lang="en">
<head>
<meta charset="utf-8">
<title>Gentle Pressure Relentlessly Applied – Leading Change</title>
<link rel="stylesheet" href="https://fonts.googleapis.com/css2?family=Raleway:wght@700;800&family=Montserrat:ital,wght@0,400;0,600;1,800&display=swap">
<style>
  :root {
    --page-bg: #eceff2;
    --card-bg: #ffffff;
    --teal-light: #1fc0dc;
    --teal: #0fa9c4;
    --teal-mid: #0f8fa1;
    --teal-deep: #137a89;
    --teal-dark: #0d4f5b;
    --ink: #1f2a2e;
    --white: #ffffff;
  }
  * { margin: 0; padding: 0; box-sizing: border-box; }
  html, body { width: 860px; height: 1200px; overflow: hidden; }
  body { background: var(--page-bg); position: relative; }
  .infographic {
    position: absolute; left: 30px; top: 374px;
    width: 800px; height: 451px;
    background: var(--card-bg);
    box-shadow: 0 6px 20px rgba(0,0,0,.12);
  }
  .infographic svg { display: block; width: 100%; height: 100%; }
  .brand-name { font-family: "Raleway", sans-serif; font-weight: 700; font-size: 19px; fill: var(--white); letter-spacing: .2px; }
  .main-title { font-family: "Raleway", sans-serif; font-weight: 800; font-size: 29px; fill: var(--white); }
  .subtitle { font-family: "Montserrat", sans-serif; font-style: italic; font-weight: 800; font-size: 25px; fill: var(--teal); }
  .step-label { font-family: "Montserrat", sans-serif; font-weight: 400; font-size: 16px; fill: var(--ink); }
  .step-pill-text { font-family: "Montserrat", sans-serif; font-weight: 600; font-size: 16px; fill: var(--white); }
  .step-number { font-family: "Montserrat", sans-serif; font-weight: 600; font-size: 12px; fill: var(--white); }
  .icon { fill: none; stroke: var(--white); stroke-width: 1.6; stroke-linecap: round; }
</style>
</head>
<body>
<main class="infographic">
  <svg viewBox="0 0 930 524" xmlns="http://www.w3.org/2000/svg">
    <defs>
      <linearGradient id="panelGradient" x1="0" y1="0" x2="1" y2="1">
        <stop offset="0" stop-color="#12b6cf"/>
        <stop offset="1" stop-color="#0aa0bd"/>
      </linearGradient>
      <linearGradient id="sceneGradient" x1="0" y1="0" x2="0" y2="1">
        <stop offset="0" stop-color="#25b9d2"/>
        <stop offset="1" stop-color="#0f8ea3"/>
      </linearGradient>
    </defs>

    <!-- header panel -->
    <path class="header-panel" fill="url(#panelGradient)"
      d="M0 0 H555 C525 95 470 125 380 150 C300 172 250 210 232 290 C215 380 262 450 250 524 H0 Z"/>
    <path class="flow-line" fill="none" stroke="#bfe8ef" stroke-width="1.5"
      d="M530 0 C500 120 380 150 360 230 C340 320 420 380 380 524"/>

    <!-- brand -->
    <circle cx="51" cy="36" r="16" fill="none" stroke="var(--white)" stroke-width="2.5"/>
    <text class="brand-name" x="74" y="43">THE HALVERN GROUP</text>

    <!-- title -->
    <text class="main-title" x="34" y="86">GENTLE PRESSURE</text>
    <text class="main-title" x="34" y="120">RELENTLESSLY APPLIED</text>

    <!-- illustration area -->
    <path role="img" aria-label="Illustration: a presenter beside a large smartphone screen with chart, location and check icons"
      fill="url(#sceneGradient)" opacity=".85"
      d="M10 230 C60 190 200 180 280 200 L290 524 H10 Z"/>

    <!-- subtitle -->
    <text class="subtitle" x="686" y="82" text-anchor="middle">"Leading Change"</text>

    <!-- cycle diagram -->
    <g class="cycle" stroke="var(--white)" stroke-width="4">
      <path fill="var(--teal-light)" d="M687 176 A121 121 0 0 1 808 297 L734 297 A47 47 0 0 0 687 250 Z"/>
      <path fill="var(--teal-mid)" d="M808 297 A121 121 0 0 1 687 418 L687 344 A47 47 0 0 0 734 297 Z"/>
      <path fill="var(--teal-deep)" d="M687 418 A121 121 0 0 1 566 297 L640 297 A47 47 0 0 0 687 344 Z"/>
      <path fill="var(--teal-dark)" d="M566 297 A121 121 0 0 1 687 176 L687 250 A47 47 0 0 0 640 297 Z"/>
    </g>
    <g class="cycle-arrows">
      <polygon fill="var(--teal-dark)" points="685,197 703,213 685,229"/>
      <polygon fill="var(--teal-light)" points="755,299 771,315 787,299"/>
      <polygon fill="var(--teal-mid)" points="689,365 671,381 689,397"/>
      <polygon fill="var(--teal-deep)" points="587,295 603,279 619,295"/>
    </g>

    <!-- step icons -->
    <g class="icon">
      <line x1="731" y1="230" x2="753" y2="230"/>
      <line x1="735" y1="237" x2="757" y2="237"/>
      <line x1="731" y1="244" x2="753" y2="244"/>
      <line x1="735" y1="251" x2="749" y2="251"/>
      <rect x="728" y="346" width="22" height="24" rx="2"/>
      <circle cx="744" cy="356" r="8"/>
      <line x1="750" y1="362" x2="758" y2="370"/>
      <circle cx="627" cy="346" r="11"/>
      <circle cx="627" cy="346" r="4"/>
      <line x1="627" y1="357" x2="627" y2="370"/>
      <circle cx="628" cy="224" r="7"/>
      <path d="M613 250 C613 238 643 238 643 250"/>
      <path d="M638 238 L646 235 L646 243 C646 248 642 250 642 250 C642 250 638 248 638 243 Z"/>
    </g>

    <!-- step numbers -->
    <g class="step-badges" fill="var(--teal-mid)" stroke="var(--white)" stroke-width="2">
      <circle cx="780" cy="209" r="11"/>
      <circle cx="780" cy="380" r="11"/>
      <circle cx="592" cy="380" r="11"/>
      <circle cx="590" cy="209" r="11"/>
    </g>
    <text class="step-number" x="780" y="213.5" text-anchor="middle">1</text>
    <text class="step-number" x="780" y="384.5" text-anchor="middle">2</text>
    <text class="step-number" x="592" y="384.5" text-anchor="middle">3</text>
    <text class="step-number" x="590" y="213.5" text-anchor="middle">4</text>

    <!-- step 4: integrity -->
    <text class="step-label" x="560" y="128" text-anchor="middle">Culture</text>
    <text class="step-label" x="560" y="147" text-anchor="middle">of Accountability</text>
    <rect x="495" y="157" width="130" height="30" rx="15" fill="var(--teal-dark)"/>
    <text class="step-pill-text" x="560" y="178" text-anchor="middle">Integrity</text>

    <!-- step 1: alignment -->
    <text class="step-label" x="811" y="128" text-anchor="middle">Agreement</text>
    <text class="step-label" x="811" y="147" text-anchor="middle">on Approach</text>
    <rect x="746" y="157" width="130" height="30" rx="15" fill="var(--teal-light)"/>
    <text class="step-pill-text" x="811" y="178" text-anchor="middle">Alignment</text>

    <!-- step 3: skills -->
    <rect x="495" y="404" width="130" height="30" rx="15" fill="var(--teal-deep)"/>
    <text class="step-pill-text" x="560" y="425" text-anchor="middle">Skills</text>
    <text class="step-label" x="560" y="455" text-anchor="middle">Training</text>
    <text class="step-label" x="560" y="474" text-anchor="middle">and Coaching</text>

    <!-- step 2: transparency -->
    <rect x="746" y="404" width="130" height="30" rx="15" fill="var(--teal-mid)"/>
    <text class="step-pill-text" x="811" y="425" text-anchor="middle">Transparency</text>
    <text class="step-label" x="811" y="455" text-anchor="middle">Metrics</text>
    <text class="step-label" x="811" y="474" text-anchor="middle">for Assurance</text>
  </svg>
</main>
</body>
</html>
```